PROFESSIONAL MODERN REDESIGN OF CURRENT WEBSITE USING ALL SAME CONTENT

I need to redesign existing website using all existing exact content. Please do not leave anything missing. Use all content.

www.brightpathpromotionsgroup.biz

Target Market(s)

Small business owners, business to business, B2B

Industry/Entity Type

Direct Marketing

Number of Pages Required

5+ page

Colors

Designer to choose colors to be used in the design.

Requirements
Must have
• Must use exact same content as www.brightpathpromotionsgroup.biz
Nice to have
• I'd like this to be an easy to read professionally designed website with all modern elements...
Should not have
• Open

```html
<!DOCTYPE html>
<html lang="en">
<head>
<meta charset="utf-8">
<title>BrightPath Promotions Group</title>
<link href="https://fonts.googleapis.com/css2?family=Montserrat:wght@400;500;600;700;800&family=Oswald:wght@600&display=swap" rel="stylesheet">
<style>
:root{
  --dark:#1b1b1b;
  --light:#f1f1f1;
  --blue:#1a7fd0;
  --blue-deep:#0f6ab6;
  --blue-btn:#0a7fe0;
  --orange:#f4a523;
  --ink:#222;
  --white:#fff;
}
*{margin:0;padding:0;box-sizing:border-box}
html,body{width:1200px;height:655px;overflow:hidden;background:var(--white);font-family:'Montserrat',sans-serif;color:var(--ink)}
.page{position:relative;width:1200px;height:655px}
.topbar{position:absolute;left:0;top:0;width:1200px;height:75px;background:var(--light)}
.topbar-dark{position:absolute;left:0;top:0;width:626px;height:75px;background:var(--dark);clip-path:polygon(0 0,100% 0,551px 100%,0 100%)}
.brand{position:absolute;left:150px;top:22px;display:flex;align-items:center;gap:10px}
.brand-mark{width:30px;height:30px;background:var(--blue);border-radius:4px}
.brand-name{font-weight:800;font-size:19px;color:var(--blue);letter-spacing:.3px;text-transform:uppercase}
.phone-badge{position:absolute;left:637px;top:16px;width:42px;height:42px;border-radius:50%;background:var(--blue);display:flex;align-items:center;justify-content:center}
.office{position:absolute;top:19px}
.office-label{font-size:11.5px;font-weight:600;color:#555;letter-spacing:.3px}
.office-num{font-size:20px;font-weight:600;color:var(--ink);margin-top:3px}
.office-usa{left:710px}
.office-intl{left:898px}
.divider{position:absolute;left:868px;top:20px;width:1px;height:38px;background:#ccc}
.nav{position:absolute;left:0;top:75px;width:1200px;height:37.5px;background:var(--blue)}
.nav-item{position:absolute;top:0;height:37.5px;line-height:37.5px;color:var(--white);font-size:11.5px;font-weight:500;text-transform:uppercase}
.nav-sep{position:absolute;top:10px;width:1px;height:18px;background:rgba(255,255,255,.35)}
.nav-login{left:823px;width:113px;background:var(--blue-deep);display:flex;align-items:center;justify-content:center;gap:8px;font-size:12.5px}
.nav-signup{left:936px;width:113px;background:var(--orange);display:flex;align-items:center;justify-content:center;gap:8px;font-size:12.5px}
.hero{position:absolute;left:0;top:112.5px;width:1200px;height:375px;background:radial-gradient(ellipse at 55% 75%,#6b6358 0%,#3d3832 45%,#25221f 100%)}
.hero-title{position:absolute;left:150px;top:74px;width:470px;font-family:'Oswald',sans-serif;font-weight:600;font-size:23.5px;line-height:39px;color:var(--white);text-transform:uppercase;white-space:nowrap}
.hero-title .accent{color:var(--orange)}
.cta{position:absolute;left:151px;top:253.5px;width:288px;height:40px;border-radius:20px;background:var(--blue-btn);color:var(--white);font-size:12.5px;font-weight:700;display:flex;align-items:center;justify-content:center;text-transform:uppercase}
.video{position:absolute;left:625px;top:60.5px;width:426px;height:240px;background:linear-gradient(90deg,#3c5a73 0%,#2b3440 40%,#6a6660 70%,#8a8377 100%);overflow:hidden}
.video-words{position:absolute;right:8px;top:16px;width:240px;text-align:center;color:var(--white);font-weight:800;line-height:1}
.video-words .small{font-size:18px;text-align:right}
.video-words .big{font-size:36px;margin-top:6px}
.play{position:absolute;left:187px;top:100px;width:51px;height:37px;border-radius:8px;background:#e62117;display:flex;align-items:center;justify-content:center}
.stats{position:absolute;left:0;top:487.5px;width:1200px;height:157.5px;background:#f6f6f6}
.stat{position:absolute;top:27px;width:160px;text-align:center;transform:translateX(-50%)}
.stat-icon{width:62px;height:62px;border-radius:50%;background:var(--blue);margin:0 auto;display:flex;align-items:center;justify-content:center}
.stat-text{margin-top:10px;font-size:12px;font-weight:500;line-height:15.5px;color:var(--ink)}
</style>
</head>
<body>
<div class="page">
  <header class="topbar">
    <div class="topbar-dark"></div>
    <div class="brand"><span class="brand-mark"></span><span class="brand-name">BrightPath Promotions</span></div>
    <div class="phone-badge">
      <svg width="20" height="20" viewBox="0 0 24 24"><path fill="#fff" d="M6.6 10.8a15 15 0 0 0 6.6 6.6l2.2-2.2c.3-.3.7-.4 1-.2 1.1.4 2.3.6 3.6.6.6 0 1 .4 1 1V20c0 .6-.4 1-1 1C10.6 21 3 13.4 3 4c0-.6.4-1 1-1h3.5c.6 0 1 .4 1 1 0 1.3.2 2.5.6 3.6.1.3 0 .7-.2 1z"/></svg>
    </div>
    <div class="office office-usa"><div class="office-label">USA OFFICE :</div><div class="office-num">555-240-7713</div></div>
    <div class="divider"></div>
    <div class="office office-intl"><div class="office-label">INTERNATIONAL :</div><div class="office-num">1-800-555-0148</div></div>
  </header>

  <nav class="nav">
    <span class="nav-item" style="left:150px">Home</span>
    <span class="nav-sep" style="left:205px"></span>
    <span class="nav-item" style="left:223px">Our Incentives</span>
    <span class="nav-sep" style="left:341px"></span>
    <span class="nav-item" style="left:359px">Samples</span>
    <span class="nav-sep" style="left:432px"></span>
    <span class="nav-item" style="left:450px">Affiliates</span>
    <span class="nav-sep" style="left:532px"></span>
    <span class="nav-item" style="left:552px">Testimonials</span>
    <span class="nav-sep" style="left:656px"></span>
    <span class="nav-item" style="left:674px">FAQ</span>
    <span class="nav-sep" style="left:720px"></span>
    <span class="nav-item" style="left:740px">Contact</span>
    <span class="nav-item nav-login">
      <svg width="14" height="14" viewBox="0 0 24 24" fill="none" stroke="#fff" stroke-width="2.2"><path d="M14 3h6v18h-6M3 12h11M10 8l4 4-4 4"/></svg>Login
    </span>
    <span class="nav-item nav-signup">
      <svg width="16" height="14" viewBox="0 0 26 22" fill="#fff"><circle cx="9" cy="6" r="5"/><path d="M0 21c0-5 4-8 9-8s9 3 9 8z"/><path d="M21 5v10M16 10h10" stroke="#fff" stroke-width="2.4"/></svg>Sign Up
    </span>
  </nav>

  <section class="hero" role="img" aria-label="Airliner on a runway at dusk">
    <h1 class="hero-title">Boost sales from your existing<br>marketing efforts creating exciting<br>promotions with <span class="accent">access to unlimited<br>quantity of our incentive certificates</span></h1>
    <a class="cta">Quick 30 Day Risk Free Trial Signup</a>
    <div class="video" role="img" aria-label="Video thumbnail with presenter in front of travel scenes">
      <div class="video-words">
        <div class="small">Unlimited Certificates</div>
        <div class="big">Marketing</div>
        <div class="big">Sales</div>
        <div class="big">Referrals</div>
        <div class="big">Repeat</div>
      </div>
      <div class="play"><svg width="18" height="18" viewBox="0 0 10 10"><path d="M2 1l7 4-7 4z" fill="#fff"/></svg></div>
    </div>
  </section>

  <section class="stats">
    <div class="stat" style="left:184px">
      <div class="stat-icon"><svg width="32" height="28" viewBox="0 0 32 28" fill="#fff"><rect x="3" y="20" width="3" height="6"/><rect x="8" y="17" width="3" height="9"/><rect x="13" y="14" width="3" height="12"/><rect x="18" y="11" width="3" height="15"/><rect x="23" y="8" width="3" height="18"/><path d="M2 16L12 7l5 4 8-8" stroke="#fff" stroke-width="2.5" fill="none"/><path d="M22 1h7v7z"/></svg></div>
      <div class="stat-text">14+ Years In<br>Business</div>
    </div>
    <div class="stat" style="left:326px">
      <div class="stat-icon"><svg width="34" height="24" viewBox="0 0 34 24" fill="#fff"><circle cx="17" cy="6" r="5"/><circle cx="8" cy="8" r="4"/><circle cx="26" cy="8" r="4"/><path d="M8 22c0-6 4-9 9-9s9 3 9 9z"/><path d="M1 21c0-5 3-8 7-8 1 0 2 0 3 1-2 2-3 4-3 7zM33 21c0-5-3-8-7-8-1 0-2 0-3 1 2 2 3 4 3 7z"/></svg></div>
      <div class="stat-text">15,000+ Clients<br>Enrolled</div>
    </div>
    <div class="stat" style="left:482px">
      <div class="stat-icon"><svg width="30" height="28" viewBox="0 0 30 28" fill="none" stroke="#fff" stroke-width="2"><rect x="2" y="2" width="26" height="18" rx="1"/><path d="M7 8h16M7 13h9"/><circle cx="21" cy="18" r="4" fill="#fff"/><path d="M19 21l-1 5 3-2 3 2-1-5"/></svg></div>
      <div class="stat-text">4+ Million Certificates<br>Distributed</div>
    </div>
    <div class="stat" style="left:657px">
      <div class="stat-icon"><svg width="28" height="30" viewBox="0 0 28 30" fill="#fff"><rect x="2" y="9" width="24" height="6"/><rect x="4" y="16" width="20" height="13"/><rect x="12.5" y="9" width="3" height="20" fill="#1a7fd0"/><path d="M14 9C10 2 6 3 7 7M14 9c4-7 8-6 7-2" stroke="#fff" stroke-width="2" fill="none"/></svg></div>
      <div class="stat-text">Hundreds Of Thousands<br>Of Redemptions</div>
    </div>
    <div class="stat" style="left:830px">
      <div class="stat-icon"><svg width="30" height="30" viewBox="0 0 30 30" fill="#fff"><rect x="2" y="13" width="6" height="15"/><path d="M10 13l6-10c2 0 3 2 2 5l-1 4h9c2 0 3 2 2 4l-3 10c-1 2-2 2-4 2H10z"/></svg></div>
      <div class="stat-text">Top Notch Customer<br>Service</div>
    </div>
    <div class="stat" style="left:988px">
      <div class="stat-icon"><svg width="30" height="24" viewBox="0 0 30 24" fill="none" stroke="#fff" stroke-width="2"><rect x="2" y="2" width="26" height="17" rx="1"/><path d="M14 8h10M14 12h10M5 6h7"/><circle cx="9" cy="12" r="3"/><path d="M7 15l-1 6 3-2 3 2-1-6"/></svg></div>
      <div class="stat-text">Licensed Seller Of<br>Travel CST #5550172</div>
    </div>
  </section>
</div>
</body>
</html>
```